new letterhead/envelope/business card design for law firm

please see attached pdf of current letterhead, envelope and business card. I am also attaching my new logo that I would like to be used. basically, I am looking to refresh and simplify my letterhead/stationary and business card, keeping the following in mind:

overall, I am going for the following look:

-simple,
-modern,
-classy,
-professional

Target Market(s)

law firm clients

Industry/Entity Type

Law Firm

Contact Information for Business Card

see attachment

Font styles to use
Sans Serif

Requirements
Must have
• overall, I am going for the following look:
• -simple,
• -modern,
• -classy,
• -professional
Nice to have
• same as above
Should not have
• no serif fonts

```html
<!DOCTYPE html>
<html lang="en">
<head>
<meta charset="utf-8">
<title>Whitford Law – Business Card</title>
<link href="https://fonts.googleapis.com/css2?family=Roboto:wght@400;700&display=swap" rel="stylesheet">
<style>
  :root {
    --navy: #1c3a66;
    --green: #2c6e3f;
    --grey: #8a8a8a;
    --paper: #ffffff;
    --backdrop: #2a2a2a;
  }
  * { margin: 0; padding: 0; box-sizing: border-box; }
  html, body { width: 1200px; height: 960px; overflow: hidden; }
  body {
    background: var(--backdrop);
    font-family: "Roboto", sans-serif;
    position: relative;
  }
  .card {
    position: absolute;
    left: 100px; top: 194px;
    width: 1000px; height: 572px;
    background: var(--paper);
  }
  .brand {
    position: absolute;
    left: 60px; top: 150px;
    width: 360px;
    text-align: center;
  }
  .brand-dot {
    width: 96px; height: 96px;
    border-radius: 50%;
    background: var(--green);
    margin: 0 auto 22px;
  }
  .brand-name {
    font-weight: 700;
    font-size: 44px;
    letter-spacing: 3px;
    color: var(--navy);
    line-height: 1;
  }
  .brand-rule {
    height: 2px;
    background: var(--green);
    margin-top: 18px;
  }
  .divider {
    position: absolute;
    left: 470px; top: 140px;
    width: 1.5px; height: 300px;
    background: var(--green);
  }
  .details {
    position: absolute;
    left: 515px; top: 120px;
    color: var(--grey);
  }
  .person-name {
    font-weight: 700;
    font-size: 29px;
    color: var(--navy);
    margin-bottom: 6px;
  }
  .credential { font-size: 22px; line-height: 30px; }
  .contacts { list-style: none; margin-top: 30px; }
  .contacts li {
    display: flex; align-items: center;
    font-size: 22px; line-height: 31px;
  }
  .contacts svg {
    width: 18px; height: 18px;
    margin-right: 14px;
    fill: none; stroke: var(--navy); stroke-width: 2;
  }
  .address { margin-top: 28px; font-size: 22px; line-height: 31px; font-style: normal; }
</style>
</head>
<body>
  <section class="card">
    <div class="brand">
      <div class="brand-dot"></div>
      <div class="brand-name">WHITFORD LAW</div>
      <div class="brand-rule"></div>
    </div>

    <div class="divider"></div>

    <div class="details">
      <h1 class="person-name">DANIEL R. WHITFORD, ESQ.</h1>
      <p class="credential">Licensed in NC and FL</p>
      <p class="credential">Board Certified in Civil Tral Law</p>

      <ul class="contacts">
        <li><svg viewBox="0 0 24 24"><path d="M5 3h4l2 5-3 2a11 11 0 0 0 6 6l2-3 5 2v4a2 2 0 0 1-2 2A17 17 0 0 1 3 5a2 2 0 0 1 2-2z"/></svg>555.214.0183</li>
        <li><svg viewBox="0 0 24 24"><rect x="6" y="2" width="12" height="20" rx="2"/><line x1="11" y1="18" x2="13" y2="18"/></svg>555.306.7724</li>
        <li><svg viewBox="0 0 24 24"><rect x="3" y="5" width="18" height="14"/><path d="M3 5l9 8 9-8"/></svg>dan@whitfordlawpa.com</li>
        <li><svg viewBox="0 0 24 24"><circle cx="12" cy="12" r="9"/><path d="M3 12h18M12 3c3 3 3 15 0 18M12 3c-3 3-3 15 0 18"/></svg>www.whitfordlawpa.com</li>
      </ul>

      <address class="address">2240 Linden Avenue, Suite 410<br>Fairview, NC 27500</address>
    </div>
  </section>
</body>
</html>
```